Our Company is Harbourline Lot Partners and we service the whole Perth Metro region. We want our flyer to grab the potential clients attention and inform them of their potential opportunity to subdivide their residential property. We would like the flyer to show our logo, contact details website and maybe one eye catching, engaging picture/photo. If the Flyer could follow the same colours as our logo that would be great. Are we able to have a A5 size flyer front and back? maybe our contact information on the back? and other services that we offer?
A lot of our potential clients aren't aware their house/land is sub dividable, or even know how to do a subdivision. We would like our flyer to educate the average residential home owner of the potential of their property and make the idea of subdividing seem and easy and accessible. Something along the lines of "Looking to Subdivide? Not sure if your property is sub-dividable? Call us now for a obligation free assessment of your property." or maybe "Subdividing you property is easier than you might think..."
We would like to advertise that we offer:-
Free Subdivision feasibility analysis of your property,
Project Management: We offer full Project Management from start to finish ensuring a hassle free subdivision (or something along those lines)-
New title's application
Updates

Target Market(s)

Residential Home owners with the potential to subdivide their property.

Industry/Entity Type

Surveyor

Colors
f78f20
c3c3c3
3176b5

Requirements
Must have
• Simple, clutter free design offering the idea of subdividing as a new, accessible opportunity to the average homeowner.

```html
<!DOCTYPE html>
<html lang="en">
<head>
<meta charset="utf-8">
<title>Harbourline Lot Partners – Subdivisions Available</title>
<link href="https://fonts.googleapis.com/css2?family=Anton&display=swap" rel="stylesheet">
<style>
  :root {
    --navy: #14253a;
    --orange: #f0561f;
    --white: #ffffff;
    --panel: rgba(255, 255, 255, 0.55);
    --sky-top: #ffffff;
    --sky-haze: #dfe3e6;
    --hills: #8e9a9c;
    --bush: #7d7a4c;
    --bush-deep: #5b5a34;
    --grass: #a6ad8a;
  }
  html, body {
    margin: 0;
    padding: 0;
    overflow: hidden;
    background: #ffffff;
  }
  .flyer {
    position: relative;
    width: 846px;
    height: 1200px;
    overflow: hidden;
    font-family: "Anton", "Impact", sans-serif;
    text-transform: uppercase;
  }
  .landscape-photo {
    position: absolute;
    inset: 0;
    background:
      linear-gradient(180deg,
        var(--sky-top) 0%,
        var(--sky-top) 12%,
        var(--sky-haze) 17%,
        var(--hills) 22%,
        var(--bush) 30%,
        var(--bush-deep) 45%,
        var(--bush) 62%,
        var(--grass) 80%,
        var(--bush-deep) 100%);
  }
  .shapes {
    position: absolute;
    inset: 0;
  }
  .brand {
    position: absolute;
    left: 40px;
    top: 118px;
    display: flex;
    align-items: center;
    gap: 14px;
    color: var(--navy);
    font-size: 40px;
    line-height: 1;
    text-transform: none;
    letter-spacing: 0.01em;
  }
  .brand-dot {
    width: 18px;
    height: 18px;
    border-radius: 50%;
    background: var(--navy);
  }
  .tilted {
    position: absolute;
    left: 0;
    width: 846px;
    text-align: center;
    transform: rotate(-3.1deg);
    transform-origin: center;
    line-height: 1;
    white-space: nowrap;
  }
  .headline-subdivisions {
    top: 318px;
    color: var(--orange);
    font-size: 96px;
    letter-spacing: 0.09em;
  }
  .headline-available {
    top: 438px;
    color: var(--white);
    font-size: 178px;
    letter-spacing: 0.01em;
  }
  .service-analysis {
    top: 636px;
    color: var(--navy);
    font-size: 44px;
  }
  .service-management {
    top: 700px;
    color: var(--orange);
    font-size: 70px;
  }
  .service-intro {
    top: 790px;
    color: var(--navy);
    font-size: 38px;
  }
  .service-detail {
    top: 838px;
    color: var(--navy);
    font-size: 32px;
    line-height: 1.18;
  }
  .service-titles {
    top: 930px;
    color: var(--orange);
    font-size: 62px;
  }
  .contact {
    top: 1055px;
    color: var(--white);
    font-size: 90px;
  }
  .contact-label {
    color: var(--orange);
    font-size: 54px;
    margin-right: 8px;
  }
</style>
</head>
<body>
  <main class="flyer">
    <div class="landscape-photo" role="img" aria-label="Photo of Perth hills bushland with gum trees and grass trees under a hazy sky"></div>

    <svg class="shapes" width="846" height="1200" viewBox="0 0 846 1200" aria-hidden="true">
      <polygon points="0,318 846,272 846,282 0,328" fill="var(--white)"/>
      <polygon points="0,334 846,288 846,418 0,458" fill="var(--navy)"/>
      <polygon points="0,598 846,570 846,1008 0,1046" fill="var(--panel)"/>
      <polygon points="0,1050 846,1010 846,1020 0,1060" fill="var(--white)"/>
      <polygon points="0,1066 846,1026 846,1200 0,1200" fill="var(--navy)"/>
    </svg>

    <div class="brand">
      <span class="brand-dot"></span>
      <span class="brand-name">Harbourline Lot Partners</span>
    </div>

    <h1 class="tilted headline-subdivisions" style="margin:0;">Subdivisions</h1>
    <p class="tilted headline-available" style="margin:0;">Available</p>

    <p class="tilted service-analysis" style="margin:0;">Free Land Development Analysis</p>
    <p class="tilted service-management" style="margin:0;">Project Management</p>
    <p class="tilted service-intro" style="margin:0;">First Time Subdividing? No Worries!</p>
    <p class="tilted service-detail" style="margin:0;">We offer full project management from start<br>to finish ensuring a hassle free subdivision</p>
    <p class="tilted service-titles" style="margin:0;">New Title’s Application</p>

    <p class="tilted contact" style="margin:0;"><span class="contact-label">Contact:</span>04XX XXX XXX</p>
  </main>
</body>
</html>
```